Rock, Paper Scissors Championship Flyer

We need a dynamic, bold and exciting flyer to promote the following event at our sports center. The event will be primarily focused for adults, but children are welcome to join

Rock, Paper, Scissors Championship - $$$ prizes
Date: June 9th, 2018
Time: 11am-4pm
Fee: $2 to enter, free for spectators
Heats to determine the overall ‘Rock, Paper, Scissors’ champion!
- Cash prizes on offer
- Live music.
- Food and beverage available for purchase

Belvorrow Sports Center, Roselle NJ
908-555-3162
www.belvorrowgrounds.example

Must include our logo (does not have to be huge) and County seal (both attached)

Colors

Designer to choose colors to be used in the design.

Requirements
Must have
• Should be fun and colorful
• The following info and attached logos:
• Rock, Paper, Scissors Championship - $$$ prizes
• Date: June 9th, 2018
• Time: 11am-4pm
• Fee: $2 to enter, free for spectators
• Heats to determine the overall ‘Rock, Paper, Scissors’ champion!
• - Cash prizes on offer
• - Live music.
• - Food and beverage available for purchase
• Belvorrow Sports Center, Roselle NJ
• 908-555-3162
• www.belvorrowgrounds.example
Nice to have
• There are a few inspirational photos attached to give an idea of what we are looking for.

```html
<!DOCTYPE html>
<html lang="en">
<head>
<meta charset="utf-8">
<title>Rock Paper Scissors Championship</title>
<link href="https://fonts.googleapis.com/css2?family=Bitter:ital,wght@0,700;1,900&family=Bungee&family=Montserrat:wght@800;900&family=Arvo:wght@700&family=Bree+Serif&display=swap" rel="stylesheet">
<style>
  :root {
    --red: #c0192a;
    --red-deep: #a21d28;
    --teal: #1f8284;
    --forest: #175e4e;
    --blue: #4f87a3;
    --panel: #d9d9dc;
    --yellow: #f8d33a;
    --white: #ffffff;
    --tree-light: #3aa35c;
    --tree-dark: #0e5a3c;
    --gold: #f6c83c;
  }
  * { margin: 0; padding: 0; box-sizing: border-box; }
  html, body { width: 880px; height: 1200px; overflow: hidden; background: #222; }
  .flyer {
    position: relative;
    width: 880px; height: 1200px; overflow: hidden;
    background: repeating-linear-gradient(135deg,
      var(--forest) 0 95px, var(--teal) 95px 190px, var(--red-deep) 190px 285px);
    font-family: "Bree Serif", Georgia, serif;
  }
  .forest {
    position: absolute; left: 0; top: 915px; width: 880px; height: 285px;
    background: linear-gradient(180deg, var(--tree-light) 0%, #1f8048 35%, var(--tree-dark) 70%);
  }
  .title-panel {
    position: absolute; left: 180px; top: 40px; width: 520px; height: 532px;
    background: var(--panel); border: 4px solid var(--blue); border-radius: 24px;
  }
  .title-rock, .title-paper, .title-scissors {
    position: absolute; left: 180px; width: 520px; text-align: center; line-height: 1;
  }
  .title-rock {
    top: 62px; color: var(--red);
    font-family: "Bitter", Georgia, serif; font-style: italic; font-weight: 900;
    font-size: 128px; letter-spacing: -4px;
  }
  .title-paper {
    top: 176px; color: var(--blue);
    font-family: "Bungee", Impact, sans-serif; font-size: 112px; letter-spacing: 4px;
  }
  .title-scissors {
    top: 282px; color: var(--red);
    font-family: "Bitter", Georgia, serif; font-weight: 700; font-size: 106px; letter-spacing: -2px;
  }
  .ribbon { position: absolute; left: 100px; top: 384px; width: 680px; height: 112px; }
  .ribbon-text {
    position: absolute; left: 100px; top: 402px; width: 680px; text-align: center;
    color: var(--white); font-family: "Montserrat", Arial, sans-serif; font-weight: 900;
    font-size: 66px; letter-spacing: 1px; line-height: 76px; transform: rotate(-1.5deg);
  }
  .hand {
    position: absolute; top: 506px; width: 132px; height: 132px; border-radius: 50%;
    background: var(--red); border: 5px solid var(--blue);
  }
  .hand-rock { left: 209px; }
  .hand-paper { left: 374px; }
  .hand-scissors { left: 537px; }
  .date-band {
    position: absolute; left: -60px; top: 640px; width: 1000px; height: 108px;
    background: var(--yellow); transform: rotate(-5deg); transform-origin: center;
    color: var(--red); font-family: "Arvo", Georgia, serif; font-weight: 700; text-align: center;
    padding-top: 14px;
  }
  .date-line { font-size: 38px; line-height: 46px; }
  .date-line .divider { margin: 0 14px; }
  .venue-line { font-size: 30px; line-height: 36px; }
  .badge { position: absolute; z-index: 2; }
  .badge svg { width: 100%; height: 100%; display: block; }
  .badge-text {
    position: absolute; inset: 0; display: flex; flex-direction: column;
    align-items: center; justify-content: center; color: var(--white);
    font-family: "Arvo", Georgia, serif; font-weight: 700; text-align: center;
  }
  .badge-music { left: 42px; top: 738px; width: 172px; height: 172px; transform: rotate(-10deg); }
  .badge-music .badge-text { font-size: 36px; line-height: 38px; }
  .badge-prizes { left: 630px; top: 708px; width: 218px; height: 218px; transform: rotate(10deg); }
  .badge-prizes .badge-text { font-size: 36px; line-height: 42px; }
  .badge-prizes .money { color: var(--gold); font-size: 48px; letter-spacing: 14px; line-height: 50px; padding-left: 14px; }
  .info {
    position: absolute; left: 220px; top: 784px; width: 440px; text-align: center;
    color: var(--white); font-size: 17px; line-height: 25px;
  }
  .entry-box {
    position: absolute; left: 180px; top: 854px; width: 520px; height: 84px;
    background: var(--panel); border: 3px solid var(--blue); border-radius: 12px;
    color: var(--red); text-align: center; font-size: 17px; line-height: 24px; padding-top: 5px;
  }
  .brand {
    position: absolute; left: 30px; top: 1080px; width: 160px;
    display: flex; flex-direction: column; align-items: center; gap: 8px;
    color: var(--white); font-family: "Bree Serif", Georgia, serif;
    font-size: 17px; line-height: 20px; text-align: center;
  }
  .brand-dot { width: 22px; height: 22px; border-radius: 50%; background: var(--white); }
  .contact {
    position: absolute; left: 200px; top: 1130px; width: 480px; text-align: center;
    color: var(--white); font-size: 17px;
  }
  .seal {
    position: absolute; left: 711px; top: 1045px; width: 110px; height: 110px;
    border-radius: 50%; background: #e8d9a8; border: 4px solid #b8954a;
  }
</style>
</head>
<body>
<main class="flyer">
  <div class="forest" role="img" aria-label="Silhouetted pine forest along the bottom"></div>

  <div class="title-panel"></div>
  <div class="title-rock">Rock</div>
  <div class="title-paper">PAPER</div>
  <div class="title-scissors">Scissors</div>

  <svg class="ribbon" viewBox="0 0 680 112" aria-hidden="true">
    <polygon points="0,28 680,10 650,56 680,102 0,108 30,68" fill="var(--red)"/>
    <polygon points="12,34 668,18 640,56 668,94 12,100 40,68" fill="var(--blue)" stroke="var(--white)" stroke-width="3"/>
  </svg>
  <div class="ribbon-text">CHAMPIONSHIP</div>

  <div class="hand hand-rock" role="img" aria-label="Gloved hand making a rock fist"></div>
  <div class="hand hand-paper" role="img" aria-label="Gloved hand held open as paper"></div>
  <div class="hand hand-scissors" role="img" aria-label="Gloved hand making scissors"></div>

  <div class="date-band">
    <div class="date-line">Saturday, June 9, 2018<span class="divider">|</span>11am - 4pm</div>
    <div class="venue-line">Belvorrow Sports Center, Roselle NJ</div>
  </div>

  <p class="info">Food and beverages available for purchase,<br>Entrance free for spectators.</p>

  <div class="entry-box">
    - 2$ to enter competition -<br>
    Multiple heats to determine the overall<br>
    ‘Rock, Paper, Scissors’ champion!
  </div>

  <div class="badge badge-music">
    <svg viewBox="-100 -100 200 200" aria-hidden="true">
      <polygon fill="var(--white)" points="100,0 84,17 92,38 72,48 71,71 48,72 38,92 17,84 0,100 -17,84 -38,92 -48,72 -71,71 -72,48 -92,38 -84,17 -100,0 -84,-17 -92,-38 -72,-48 -71,-71 -48,-72 -38,-92 -17,-84 0,-100 17,-84 38,-92 48,-72 71,-71 72,-48 92,-38 84,-17"/>
      <polygon fill="var(--red)" transform="scale(0.9)" points="100,0 84,17 92,38 72,48 71,71 48,72 38,92 17,84 0,100 -17,84 -38,92 -48,72 -71,71 -72,48 -92,38 -84,17 -100,0 -84,-17 -92,-38 -72,-48 -71,-71 -48,-72 -38,-92 -17,-84 0,-100 17,-84 38,-92 48,-72 71,-71 72,-48 92,-38 84,-17"/>
    </svg>
    <div class="badge-text"><span>Live</span><span>Music</span></div>
  </div>

  <div class="badge badge-prizes">
    <svg viewBox="-100 -100 200 200" aria-hidden="true">
      <polygon fill="var(--white)" points="100,0 84,17 92,38 72,48 71,71 48,72 38,92 17,84 0,100 -17,84 -38,92 -48,72 -71,71 -72,48 -92,38 -84,17 -100,0 -84,-17 -92,-38 -72,-48 -71,-71 -48,-72 -38,-92 -17,-84 0,-100 17,-84 38,-92 48,-72 71,-71 72,-48 92,-38 84,-17"/>
      <polygon fill="var(--red)" transform="scale(0.92)" points="100,0 84,17 92,38 72,48 71,71 48,72 38,92 17,84 0,100 -17,84 -38,92 -48,72 -71,71 -72,48 -92,38 -84,17 -100,0 -84,-17 -92,-38 -72,-48 -71,-71 -48,-72 -38,-92 -17,-84 0,-100 17,-84 38,-92 48,-72 71,-71 72,-48 92,-38 84,-17"/>
    </svg>
    <div class="badge-text"><span>Win</span><span class="money">$$$</span><span>Prizes!</span></div>
  </div>

  <div class="brand">
    <span class="brand-dot"></span>
    <span>Belvorrow Sports Center</span>
  </div>

  <p class="contact">908-555-3162 - www.belvorrowgrounds.example</p>

  <div class="seal" role="img" aria-label="County seal"></div>
</main>
</body>
</html>
```